People/Expertise finder to associate people to experts, services and products

Design a mock-up for a people finder/expertise finder system. The people/expertise finder project is targeting to relate people to experts, countries and core operations. We are expecting the final UI to be responsive. The styleguide that is followed in the enterprise is attached for reference. further documents outlining the vision is also attached. Based on queries kindly use the crew deck profile as an example of profile page. People will search using the enterprise search on names, skills etc to find matching people.

Logo Text

People Finder

Number of Pages Required

3 page

Requirements
Must have
• The UI should be aesthetically good and should bring in the industry standards

```html
<!DOCTYPE html>
<html lang="en">
<head>
<meta charset="utf-8">
<title>Find People – Search Results</title>
<link rel="stylesheet" href="https://fonts.googleapis.com/css2?family=Open+Sans:wght@400;600;700&display=swap">
<style>
  :root{
    --navy:#0d2b52;
    --page-bg:#eeedf1;
    --card:#ffffff;
    --blue:#1a73d9;
    --link-blue:#2b7bc0;
    --text:#1f1f1f;
    --muted:#6b6b6b;
    --line:#e6e6ea;
    --star:#f2b01e;
    --photo:#bdbdbd;
  }
  *{box-sizing:border-box;margin:0;padding:0}
  html,body{width:1200px;height:1200px;overflow:hidden;background:#ffffff;font-family:"Open Sans",Arial,sans-serif;color:var(--text)}
  .page{position:absolute;left:95px;top:0;width:1010px;height:1200px;background:var(--page-bg)}
  .topbar{position:absolute;left:0;top:0;width:1010px;height:45px;background:var(--navy);border-bottom:2px solid #1c4a86}
  .brand{position:absolute;left:122px;top:9px;display:flex;align-items:center;gap:9px;color:#fff;font-size:13px;font-weight:600;letter-spacing:.2px}
  .brand-dot{width:26px;height:26px;border-radius:50%;background:#fff}
  .topbar-actions{position:absolute;left:705px;top:0;height:45px;display:flex;align-items:center;gap:12px;color:#fff;font-size:11px}
  .icon-badge{position:relative;width:18px;height:16px}
  .icon-badge .count{position:absolute;right:-6px;top:-5px;background:var(--blue);color:#fff;font-size:7px;width:10px;height:10px;border-radius:50%;text-align:center;line-height:10px}
  .user{display:flex;align-items:center;gap:7px;margin-left:24px}
  .user-photo{width:26px;height:26px;border-radius:50%;background:linear-gradient(135deg,#e7c7a9,#8a6a52)}
  .search{position:absolute;left:121px;top:64px;width:450px;height:34px;background:#fff;border:1px solid var(--line);font-size:11px;padding:10px 12px;color:#333}
  .search-btn{position:absolute;left:581px;top:64px;width:112px;height:34px;background:var(--blue);color:#fff;font-size:10px;font-weight:700;display:flex;align-items:center;justify-content:center;gap:7px}
  .result-count{position:absolute;left:121px;top:109px;font-size:9.5px;color:#333}
  .result-count b{font-weight:700}
  .results{position:absolute;left:121px;top:135px;width:572px;height:1049px;background:var(--card);box-shadow:0 1px 2px rgba(0,0,0,.06)}
  .tabs{display:flex;height:35px;border-bottom:1px solid var(--line)}
  .tab{font-size:9.5px;color:#333;padding:0 15px;display:flex;align-items:center;border-right:1px solid var(--line)}
  .tab.active{border-bottom:3px solid var(--navy)}
  .person{position:relative;height:183px;border-bottom:1px solid var(--line)}
  .avatar{position:absolute;left:22px;top:21px;width:45px;height:45px;border-radius:50%;background:linear-gradient(160deg,#d6d6d6,var(--photo) 60%,#8d8d8d)}
  .name-row{position:absolute;left:81px;top:19px;display:flex;align-items:center;gap:6px}
  .name{font-size:10.5px;font-weight:700;color:#333;letter-spacing:.2px}
  .stars{display:flex;gap:1px}
  .role{position:absolute;left:81px;top:35px;font-size:7.5px;color:var(--muted);font-weight:600}
  .view-btn{position:absolute;left:471px;top:21px;width:81px;height:19px;border:1px solid var(--link-blue);color:var(--link-blue);font-size:7.5px;display:flex;align-items:center;justify-content:center;letter-spacing:.3px}
  .rule{position:absolute;left:81px;right:0;top:50px;height:1px;background:var(--line)}
  .links{position:absolute;left:89px;top:59px;display:flex;align-items:center;gap:10px}
  .crew-deck{font-size:7.5px;font-weight:600;color:var(--link-blue)}
  .contact{position:absolute;left:81px;top:86px;font-size:8px;line-height:1.1}
  .contact dt{font-size:5.5px;color:#8a8a8a;font-weight:700;letter-spacing:.4px;margin-top:6px}
  .contact dt:first-child{margin-top:0}
  .contact dd{margin-top:4px;color:#333}
  .work{position:absolute;left:224px;top:88px;width:335px;font-size:8.3px;line-height:16px;color:#333}
  .work h3{font-size:8.5px;font-weight:700;margin-bottom:4px}
  .work-rule{position:absolute;left:224px;right:0;top:150px;height:1px;background:var(--line)}
  .filters{position:absolute;left:712px;top:64px;width:177px;height:249px;background:var(--card);box-shadow:0 1px 2px rgba(0,0,0,.06)}
  .filters h2{font-size:8.5px;font-weight:700;color:#222;padding:12px 14px;border-bottom:1px solid var(--line);letter-spacing:.2px}
  .filter{padding:0 14px;margin-top:14px}
  .filter label{display:block;font-size:6.5px;color:#444;margin-bottom:4px}
  .select{position:relative;width:149px;height:20px;border:1px solid #d6d6da;font-size:7.5px;color:#888;padding:5px 6px}
  .select::after{content:"";position:absolute;right:7px;top:8px;border:4px solid transparent;border-top-color:#a7a7a7}
</style>
</head>
<body>
<div class="page">
  <header class="topbar">
    <div class="brand"><span class="brand-dot"></span>FIND PEOPLE</div>
    <div class="topbar-actions">
      <div class="icon-badge">
        <svg width="16" height="12" viewBox="0 0 16 12"><rect x="0.5" y="0.5" width="15" height="11" fill="#fff"/><path d="M1 1l7 6 7-6" stroke="#0d2b52" fill="none"/></svg>
        <span class="count">1</span>
      </div>
      <div class="icon-badge">
        <svg width="14" height="15" viewBox="0 0 14 15"><path d="M7 1c-3 0-4.5 2.3-4.5 5v3L1 11h12l-1.5-2V6C11.5 3.3 10 1 7 1z" fill="#fff"/><circle cx="7" cy="13" r="1.6" fill="#fff"/></svg>
        <span class="count">4</span>
      </div>
      <div class="user">
        <span class="user-photo" role="img" aria-label="Photo of the signed-in user"></span>
        <span>Hello Ada</span>
        <svg width="9" height="6" viewBox="0 0 9 6"><path d="M1 1l3.5 3.5L8 1" stroke="#fff" stroke-width="1.8" fill="none"/></svg>
      </div>
    </div>
  </header>

  <div class="search">Pell</div>
  <div class="search-btn">
    <svg width="14" height="14" viewBox="0 0 14 14"><circle cx="6" cy="6" r="4.6" stroke="#fff" stroke-width="2" fill="none"/><path d="M9.5 9.5L13 13" stroke="#fff" stroke-width="2"/></svg>
    SEARCH
  </div>
  <p class="result-count"><b>292,816 results -</b> people for Pell</p>

  <section class="results">
    <nav class="tabs">
      <span class="tab active">People</span>
      <span class="tab">Country</span>
      <span class="tab">Program</span>
      <span class="tab">Most Reviewed</span>
      <span class="tab">Most Popular</span>
    </nav>

    <article class="person">
      <span class="avatar" role="img" aria-label="Profile photo of Nora Pell"></span>
      <div class="name-row"><span class="name">NORA PELL</span>
        <svg class="stars" width="58" height="10" viewBox="0 0 58 10"><g fill="#f2b01e"><path d="M5 0l1.5 3.2 3.5.4-2.6 2.4.7 3.5L5 7.8 1.9 9.5l.7-3.5L0 3.6l3.5-.4z"/><path transform="translate(12)" d="M5 0l1.5 3.2 3.5.4-2.6 2.4.7 3.5L5 7.8 1.9 9.5l.7-3.5L0 3.6l3.5-.4z"/><path transform="translate(24)" d="M5 0l1.5 3.2 3.5.4-2.6 2.4.7 3.5L5 7.8 1.9 9.5l.7-3.5L0 3.6l3.5-.4z"/><path transform="translate(36)" d="M5 0v7.8L1.9 9.5l.7-3.5L0 3.6l3.5-.4z"/></g><g fill="none" stroke="#f2b01e" stroke-width=".8"><path transform="translate(36)" d="M5 0l1.5 3.2 3.5.4-2.6 2.4.7 3.5L5 7.8"/><path transform="translate(48)" d="M5 .5l1.4 3 3.2.4-2.4 2.2.6 3.2L5 7.7 2.2 9.3l.6-3.2L.4 3.9l3.2-.4z"/></g></svg>
      </div>
      <p class="role">Project manager, SPR, SP</p>
      <span class="view-btn">VIEW PROFILE</span>
      <span class="rule"></span>
      <div class="links">
        <span class="crew-deck">crew deck</span>
        <svg width="10" height="12" viewBox="0 0 10 12"><path d="M1 .5h5.5L9 3v8.5H1z M3 5h4M3 7h4M3 9h3" stroke="#2b7bc0" fill="none"/></svg>
        <svg width="12" height="11" viewBox="0 0 12 11"><g fill="#2b7bc0"><rect x="4" y="0" width="4" height="3"/><rect x="0" y="7" width="3.4" height="3"/><rect x="4.3" y="7" width="3.4" height="3"/><rect x="8.6" y="7" width="3.4" height="3"/></g><path d="M6 3v2M1.7 7V5h8.6v2M6 5v2" stroke="#2b7bc0" fill="none"/></svg>
      </div>
      <dl class="contact">
        <dt>PHONE</dt><dd>(+31) 100 555 013</dd>
        <dt>EMAIL</dt><dd>norapell@mailbox.test</dd>
        <dt>ROOM NUMBER</dt><dd>Lindelaan 12, Havenstad</dd>
      </dl>
      <div class="work"><h3>I work on</h3>Structured Routing of Orders in Purchasing (SROP) and procurement systems<br>as well as Data Analytics</div>
      <span class="work-rule"></span>
    </article>

    <article class="person">
      <span class="avatar" role="img" aria-label="Profile photo of Nora Pell"></span>
      <div class="name-row"><span class="name">NORA PELL</span>
        <svg class="stars" width="58" height="10" viewBox="0 0 58 10"><g fill="#f2b01e"><path d="M5 0l1.5 3.2 3.5.4-2.6 2.4.7 3.5L5 7.8 1.9 9.5l.7-3.5L0 3.6l3.5-.4z"/><path transform="translate(12)" d="M5 0l1.5 3.2 3.5.4-2.6 2.4.7 3.5L5 7.8 1.9 9.5l.7-3.5L0 3.6l3.5-.4z"/><path transform="translate(24)" d="M5 0l1.5 3.2 3.5.4-2.6 2.4.7 3.5L5 7.8 1.9 9.5l.7-3.5L0 3.6l3.5-.4z"/><path transform="translate(36)" d="M5 0v7.8L1.9 9.5l.7-3.5L0 3.6l3.5-.4z"/></g><g fill="none" stroke="#f2b01e" stroke-width=".8"><path transform="translate(36)" d="M5 0l1.5 3.2 3.5.4-2.6 2.4.7 3.5L5 7.8"/><path transform="translate(48)" d="M5 .5l1.4 3 3.2.4-2.4 2.2.6 3.2L5 7.7 2.2 9.3l.6-3.2L.4 3.9l3.2-.4z"/></g></svg>
      </div>
      <p class="role">Project manager, SPR, SP</p>
      <span class="view-btn">VIEW PROFILE</span>
      <span class="rule"></span>
      <div class="links">
        <span class="crew-deck">crew deck</span>
        <svg width="10" height="12" viewBox="0 0 10 12"><path d="M1 .5h5.5L9 3v8.5H1z M3 5h4M3 7h4M3 9h3" stroke="#2b7bc0" fill="none"/></svg>
        <svg width="12" height="11" viewBox="0 0 12 11"><g fill="#2b7bc0"><rect x="4" y="0" width="4" height="3"/><rect x="0" y="7" width="3.4" height="3"/><rect x="4.3" y="7" width="3.4" height="3"/><rect x="8.6" y="7" width="3.4" height="3"/></g><path d="M6 3v2M1.7 7V5h8.6v2M6 5v2" stroke="#2b7bc0" fill="none"/></svg>
      </div>
      <dl class="contact">
        <dt>PHONE</dt><dd>(+31) 100 555 013</dd>
        <dt>EMAIL</dt><dd>norapell@mailbox.test</dd>
        <dt>ROOM NUMBER</dt><dd>Lindelaan 12, Havenstad</dd>
      </dl>
      <div class="work"><h3>I work on</h3>Structured Routing of Orders in Purchasing (SROP) and procurement systems<br>as well as Data Analytics</div>
      <span class="work-rule"></span>
    </article>

    <article class="person">
      <span class="avatar" role="img" aria-label="Profile photo of Nora Pell"></span>
      <div class="name-row"><span class="name">NORA PELL</span>
        <svg class="stars" width="58" height="10" viewBox="0 0 58 10"><g fill="#f2b01e"><path d="M5 0l1.5 3.2 3.5.4-2.6 2.4.7 3.5L5 7.8 1.9 9.5l.7-3.5L0 3.6l3.5-.4z"/><path transform="translate(12)" d="M5 0l1.5 3.2 3.5.4-2.6 2.4.7 3.5L5 7.8 1.9 9.5l.7-3.5L0 3.6l3.5-.4z"/><path transform="translate(24)" d="M5 0l1.5 3.2 3.5.4-2.6 2.4.7 3.5L5 7.8 1.9 9.5l.7-3.5L0 3.6l3.5-.4z"/><path transform="translate(36)" d="M5 0v7.8L1.9 9.5l.7-3.5L0 3.6l3.5-.4z"/></g><g fill="none" stroke="#f2b01e" stroke-width=".8"><path transform="translate(36)" d="M5 0l1.5 3.2 3.5.4-2.6 2.4.7 3.5L5 7.8"/><path transform="translate(48)" d="M5 .5l1.4 3 3.2.4-2.4 2.2.6 3.2L5 7.7 2.2 9.3l.6-3.2L.4 3.9l3.2-.4z"/></g></svg>
      </div>
      <p class="role">Project manager, SPR, SP</p>
      <span class="view-btn">VIEW PROFILE</span>
      <span class="rule"></span>
      <div class="links">
        <span class="crew-deck">crew deck</span>
        <svg width="10" height="12" viewBox="0 0 10 12"><path d="M1 .5h5.5L9 3v8.5H1z M3 5h4M3 7h4M3 9h3" stroke="#2b7bc0" fill="none"/></svg>
        <svg width="12" height="11" viewBox="0 0 12 11"><g fill="#2b7bc0"><rect x="4" y="0" width="4" height="3"/><rect x="0" y="7" width="3.4" height="3"/><rect x="4.3" y="7" width="3.4" height="3"/><rect x="8.6" y="7" width="3.4" height="3"/></g><path d="M6 3v2M1.7 7V5h8.6v2M6 5v2" stroke="#2b7bc0" fill="none"/></svg>
      </div>
      <dl class="contact">
        <dt>PHONE</dt><dd>(+31) 100 555 013</dd>
        <dt>EMAIL</dt><dd>norapell@mailbox.test</dd>
        <dt>ROOM NUMBER</dt><dd>Lindelaan 12, Havenstad</dd>
      </dl>
      <div class="work"><h3>I work on</h3>Structured Routing of Orders in Purchasing (SROP) and procurement systems<br>as well as Data Analytics</div>
      <span class="work-rule"></span>
    </article>

    <article class="person">
      <span class="avatar" role="img" aria-label="Profile photo of Nora Pell"></span>
      <div class="name-row"><span class="name">NORA PELL</span>
        <svg class="stars" width="58" height="10" viewBox="0 0 58 10"><g fill="#f2b01e"><path d="M5 0l1.5 3.2 3.5.4-2.6 2.4.7 3.5L5 7.8 1.9 9.5l.7-3.5L0 3.6l3.5-.4z"/><path transform="translate(12)" d="M5 0l1.5 3.2 3.5.4-2.6 2.4.7 3.5L5 7.8 1.9 9.5l.7-3.5L0 3.6l3.5-.4z"/><path transform="translate(24)" d="M5 0l1.5 3.2 3.5.4-2.6 2.4.7 3.5L5 7.8 1.9 9.5l.7-3.5L0 3.6l3.5-.4z"/><path transform="translate(36)" d="M5 0v7.8L1.9 9.5l.7-3.5L0 3.6l3.5-.4z"/></g><g fill="none" stroke="#f2b01e" stroke-width=".8"><path transform="translate(36)" d="M5 0l1.5 3.2 3.5.4-2.6 2.4.7 3.5L5 7.8"/><path transform="translate(48)" d="M5 .5l1.4 3 3.2.4-2.4 2.2.6 3.2L5 7.7 2.2 9.3l.6-3.2L.4 3.9l3.2-.4z"/></g></svg>
      </div>
      <p class="role">Project manager, SPR, SP</p>
      <span class="view-btn">VIEW PROFILE</span>
      <span class="rule"></span>
      <div class="links">
        <span class="crew-deck">crew deck</span>
        <svg width="10" height="12" viewBox="0 0 10 12"><path d="M1 .5h5.5L9 3v8.5H1z M3 5h4M3 7h4M3 9h3" stroke="#2b7bc0" fill="none"/></svg>
        <svg width="12" height="11" viewBox="0 0 12 11"><g fill="#2b7bc0"><rect x="4" y="0" width="4" height="3"/><rect x="0" y="7" width="3.4" height="3"/><rect x="4.3" y="7" width="3.4" height="3"/><rect x="8.6" y="7" width="3.4" height="3"/></g><path d="M6 3v2M1.7 7V5h8.6v2M6 5v2" stroke="#2b7bc0" fill="none"/></svg>
      </div>
      <dl class="contact">
        <dt>PHONE</dt><dd>(+31) 100 555 013</dd>
        <dt>EMAIL</dt><dd>norapell@mailbox.test</dd>
        <dt>ROOM NUMBER</dt><dd>Lindelaan 12, Havenstad</dd>
      </dl>
      <div class="work"><h3>I work on</h3>Structured Routing of Orders in Purchasing (SROP) and procurement systems<br>as well as Data Analytics</div>
      <span class="work-rule"></span>
    </article>

    <article class="person">
      <span class="avatar" role="img" aria-label="Profile photo of Nora Pell"></span>
      <div class="name-row"><span class="name">NORA PELL</span>
        <svg class="stars" width="58" height="10" viewBox="0 0 58 10"><g fill="#f2b01e"><path d="M5 0l1.5 3.2 3.5.4-2.6 2.4.7 3.5L5 7.8 1.9 9.5l.7-3.5L0 3.6l3.5-.4z"/><path transform="translate(12)" d="M5 0l1.5 3.2 3.5.4-2.6 2.4.7 3.5L5 7.8 1.9 9.5l.7-3.5L0 3.6l3.5-.4z"/><path transform="translate(24)" d="M5 0l1.5 3.2 3.5.4-2.6 2.4.7 3.5L5 7.8 1.9 9.5l.7-3.5L0 3.6l3.5-.4z"/><path transform="translate(36)" d="M5 0v7.8L1.9 9.5l.7-3.5L0 3.6l3.5-.4z"/></g><g fill="none" stroke="#f2b01e" stroke-width=".8"><path transform="translate(36)" d="M5 0l1.5 3.2 3.5.4-2.6 2.4.7 3.5L5 7.8"/><path transform="translate(48)" d="M5 .5l1.4 3 3.2.4-2.4 2.2.6 3.2L5 7.7 2.2 9.3l.6-3.2L.4 3.9l3.2-.4z"/></g></svg>
      </div>
      <p class="role">Project manager, SPR, SP</p>
      <span class="view-btn">VIEW PROFILE</span>
      <span class="rule"></span>
      <div class="links">
        <span class="crew-deck">crew deck</span>
        <svg width="10" height="12" viewBox="0 0 10 12"><path d="M1 .5h5.5L9 3v8.5H1z M3 5h4M3 7h4M3 9h3" stroke="#2b7bc0" fill="none"/></svg>
        <svg width="12" height="11" viewBox="0 0 12 11"><g fill="#2b7bc0"><rect x="4" y="0" width="4" height="3"/><rect x="0" y="7" width="3.4" height="3"/><rect x="4.3" y="7" width="3.4" height="3"/><rect x="8.6" y="7" width="3.4" height="3"/></g><path d="M6 3v2M1.7 7V5h8.6v2M6 5v2" stroke="#2b7bc0" fill="none"/></svg>
      </div>
      <dl class="contact">
        <dt>PHONE</dt><dd>(+31) 100 555 013</dd>
        <dt>EMAIL</dt><dd>norapell@mailbox.test</dd>
        <dt>ROOM NUMBER</dt><dd>Lindelaan 12, Havenstad</dd>
      </dl>
      <div class="work"><h3>I work on</h3>Structured Routing of Orders in Purchasing (SROP) and procurement systems<br>as well as Data Analytics</div>
      <span class="work-rule"></span>
    </article>
  </section>

  <aside class="filters">
    <h2>FILTER SEARCH RESULTS</h2>
    <div class="filter"><label>COUNTRY</label><div class="select">United States</div></div>
    <div class="filter"><label>SKILLS</label><div class="select"></div></div>
    <div class="filter"><label>DEPARTMENT/ DIVISION</label><div class="select"></div></div>
    <div class="filter"><label>PUBLICATION</label><div class="select"></div></div>
  </aside>
</div>
</body>
</html>
```